Melbourne Gym Celebrating 49 years of business

We are celebrating our 49th birthday and will be running a "12 month Membership Special" $299.00 save over 30%. Being one of the longest running gyms in the fitness industry the design must be very eye catching and professional in its appearance. Given the length of operation, artwork must also have a touch of class that will appeal to 18-40 year old's. Below are previous specials with its layout and sample 49th Anniversary layouts. The final design should emphasis the advertised sale, along with celebrating 49 years. You can be as creative as possible with layout and design.

Target Market(s)

Male and females aged between 18-40

Font styles to use
Serif
Sans Serif

Requirements
Must have
• Must emphasize either "Celebrating 49 years" "49th Anniversary" or Happy 49th Birthday" and in a large font "12 Month Special $299.00 SAVE OVER 30%" Terms and Conditions Apply, Strictly Limited Time Only.
• "contact details"
• Address: 14 Harlow Rd Tindale Park
• Ph: 9517 2860
• www.corvalfitness.com.au
• Design format must come in poster size A0 size, Instagram format, Facebook cover and 800 x 800 for the website
Nice to have
• Given the number of years in business, an elegant/classy feel would be nice to the overall presentation. Bright colors can be used along with artistic graphic designs

```html
<!DOCTYPE html>
<html lang="en">
<head>
<meta charset="utf-8">
<title>Corval Fitness – 49th Anniversary A0 Poster</title>
<link rel="stylesheet" href="https://fonts.googleapis.com/css2?family=Oswald:wght@300;400;500;600;700&display=swap">
<style>
  :root {
    --page-bg: #ffffff;
    --label-ink: #3a3a3a;
    --poster-deep: #141b2b;
    --poster-mid: #2c3850;
    --poster-light: #51607a;
    --ink-white: #ffffff;
    --ink-soft: #d9dde6;
    --badge-fill: rgba(10, 14, 24, 0.6);
    --photo-dark: #1a1f2b;
    --photo-warm: #8a6a58;
  }
  * { margin: 0; padding: 0; box-sizing: border-box; }
  html, body {
    width: 800px; height: 1200px; overflow: hidden;
    background: var(--page-bg);
    font-family: "Oswald", "Arial Narrow", sans-serif;
  }
  .sheet { position: relative; width: 800px; height: 1200px; }

  .sheet-label {
    position: absolute; top: 52px; left: 0; width: 100%;
    text-align: center; color: var(--label-ink);
  }
  .sheet-label__title { font-size: 42px; font-weight: 600; line-height: 1; letter-spacing: 1px; }
  .sheet-label__sub { font-size: 24px; font-weight: 400; line-height: 1.3; letter-spacing: 1px; }

  .poster {
    position: absolute; left: 59px; top: 160px; width: 682px; height: 987px;
    overflow: hidden; color: var(--ink-white);
    background:
      radial-gradient(ellipse at 40% 25%, var(--poster-light) 0%, transparent 55%),
      radial-gradient(ellipse at 20% 80%, var(--poster-mid) 0%, transparent 60%),
      linear-gradient(160deg, var(--poster-mid) 0%, var(--poster-deep) 70%);
  }

  .poster__photo {
    position: absolute; right: 0; top: 70px; width: 360px; height: 870px;
    background:
      radial-gradient(ellipse at 50% 18%, var(--photo-warm) 0%, transparent 35%),
      radial-gradient(ellipse at 45% 55%, rgba(138,106,88,0.6) 0%, transparent 50%),
      linear-gradient(180deg, transparent 0%, var(--photo-dark) 100%);
  }

  .poster__brand-top {
    position: absolute; top: 40px; left: 0; width: 100%;
    text-align: center; font-size: 30px; font-weight: 400; letter-spacing: 2px;
  }

  .headline { position: absolute; left: 58px; top: 150px; }
  .headline__number {
    display: flex; align-items: flex-start;
    font-weight: 500; line-height: 0.85;
  }
  .headline__digits { font-size: 230px; letter-spacing: -4px; }
  .headline__suffix { font-size: 100px; margin-left: 8px; margin-top: 6px; }
  .headline__word { font-size: 92px; font-weight: 500; line-height: 1; margin-top: 22px; letter-spacing: 1px; }

  .offer { position: absolute; left: 62px; top: 488px; }
  .offer__title { font-size: 44px; font-weight: 500; line-height: 1; letter-spacing: 1px; }
  .offer__price {
    margin-top: 12px; width: 282px; height: 60px;
    border: 3px solid var(--ink-white);
    display: flex; align-items: center; justify-content: center;
    font-size: 40px; font-weight: 500; line-height: 1;
  }

  .saving-badge {
    position: absolute; left: 52px; top: 626px; width: 236px; height: 236px;
    border-radius: 50%; background: var(--badge-fill);
    display: flex; flex-direction: column; align-items: center; justify-content: center;
  }
  .saving-badge__label { font-size: 40px; font-weight: 500; line-height: 1; }
  .saving-badge__value { font-size: 96px; font-weight: 600; line-height: 1; }

  .terms {
    position: absolute; left: 40px; top: 872px; width: 260px;
    text-align: center; font-size: 11px; font-weight: 400; letter-spacing: 0.5px;
    color: var(--ink-soft); text-transform: uppercase; line-height: 1.35;
  }

  .brand-mark {
    position: absolute; left: 300px; top: 848px; width: 200px;
    text-align: center; font-size: 28px; font-weight: 700; line-height: 1; letter-spacing: 1px;
  }

  .contact-bar {
    position: absolute; left: 0; bottom: 26px; width: 100%;
    display: flex; justify-content: space-between; padding: 0 30px;
    font-size: 15px; font-weight: 400; letter-spacing: 0.5px; color: var(--ink-soft);
    text-transform: uppercase;
  }
</style>
</head>
<body>
  <main class="sheet">
    <header class="sheet-label">
      <div class="sheet-label__title">A0 POSTER</div>
      <div class="sheet-label__sub">DRAFT DESIGN</div>
    </header>

    <section class="poster">
      <div class="poster__photo" role="img" aria-label="Photo of a woman in black sportswear holding a dumbbell, looking over her shoulder"></div>

      <div class="poster__brand-top">CORVAL FITNESS</div>

      <div class="headline">
        <div class="headline__number">
          <span class="headline__digits">49</span><span class="headline__suffix">TH</span>
        </div>
        <div class="headline__word">ANNIVERSARY</div>
      </div>

      <div class="offer">
        <div class="offer__title">12 MONTH SPECIAL</div>
        <div class="offer__price">$299.00</div>
      </div>

      <div class="saving-badge">
        <div class="saving-badge__label">SAVE OVER</div>
        <div class="saving-badge__value">30%</div>
      </div>

      <div class="terms">Terms and conditions apply<br>Strictly limited time only</div>

      <div class="brand-mark">CORVAL<br>FITNESS</div>

      <footer class="contact-bar">
        <span>Address: 14 Harlow Rd Tindale Park</span>
        <span>Ph: 9517 2860</span>
        <span>www.corvalfitness.com.au</span>
      </footer>
    </section>
  </main>
</body>
</html>
```